Car Soap Label Design specifically targeting RVs

I am private labeling a car wash soap to specifically target the RV industry. It will be sold in a one gallon jug with a 6"x11" spot to place the label on front and wrap around the two sides. (see attached pics for example of label size) The front of the label I want to have a realistic picture of a high dollar class A RV somehow integrated into the design, and the key features of the soap. I had wordsmithbot design a couple that I kind of like the look of that I will attach, but open to other options. I want something clean and professional looking that will back the premium product I am selling.
The name of my brand is "Blue Harbor Gleam". I want the brand name to be somewhere on the label, but not a main focus. I want the focus to be the product and its benefits. "Premium RV Wash and Wax" as the main verbiage. Benefits... "Developed for Use With Foam Gun or Bucket with Water", "Safe for All RV Exteriors", "Protective Wax Formula", "Enhanced Shine", "Water Repellent", "Streak Free Rinse", "UV Protection". On the side...Directions: 2 Ways of Mixing... Pour Concentrate into Foam Gun Bottle OR Mixing Ratio: 1 Part Wash & Wax / 3 Parts Water in bucket. Apply soap to one side of RV at a time and use carwash brush to easily loosen road film and rinse clean. On the other side... Keep from freezing, Keep Out of Reach of Children. MADE IN USA. Hazardous Ingredients: NONE . NOTICE: The seller and/or manufacturer assumes no responsibility for damage or injury resulting from misuse of this product. No warranties, expressed or implied, are given for the performance or safety of this product.

Target Market(s)

RV industry

Industry/Entity Type

RV/Auto

Requirements
Must have
• Clean, Professional look, size 6" tall and 11" wide
Nice to have
• Realistic Class A RV as part of design

```html
<!DOCTYPE html>
<html lang="en">
<head>
<meta charset="utf-8">
<title>Premium RV Wash &amp; Wax Label</title>
<link href="https://fonts.googleapis.com/css2?family=Roboto+Condensed:wght@400;700;900&family=Open+Sans:wght@400;600;700&display=swap" rel="stylesheet">
<style>
  :root {
    --page-bg: #e9ebee;
    --label-base: #f5f7f9;
    --brand-blue: #1b9bd7;
    --deep-blue: #0f7fb8;
    --navy: #1c2733;
    --tab-orange: #f2a23a;
    --white: #ffffff;
    --rv-light: #e4e8ec;
    --rv-dark: #9aa3ad;
  }
  * { box-sizing: border-box; margin: 0; padding: 0; }
  html, body { width: 885px; height: 1200px; overflow: hidden; }
  body {
    background: var(--page-bg);
    font-family: "Open Sans", sans-serif;
    position: relative;
  }
  .label {
    position: absolute;
    left: 20px; top: 370px;
    width: 845px; height: 461px;
    background: var(--label-base);
    overflow: hidden;
    box-shadow: 0 2px 8px rgba(0,0,0,.12);
  }
  .label-bg { position: absolute; inset: 0; }
  .rv-visual {
    position: absolute;
    left: 14px; top: 22px; width: 360px; height: 214px;
    border-radius: 10px;
    background: linear-gradient(160deg, var(--rv-light), var(--rv-dark));
  }
  .size-badge {
    position: absolute; left: 356px; top: 22px;
    width: 68px; height: 68px; border-radius: 50%;
    background: var(--brand-blue); color: var(--white);
    border: 3px solid var(--white);
    text-align: center; font-family: "Roboto Condensed", sans-serif;
  }
  .size-badge .qty { display: block; font-size: 26px; font-weight: 900; line-height: 30px; margin-top: 6px; }
  .size-badge .unit { display: block; font-size: 10px; font-weight: 700; }
  .brand-name {
    position: absolute; left: 24px; top: 252px;
    color: var(--brand-blue); font-size: 15px; font-weight: 600;
  }
  .product-title {
    position: absolute; left: 22px; top: 270px;
    font-family: "Roboto Condensed", sans-serif; font-weight: 400;
    font-size: 52px; color: var(--navy); letter-spacing: 1px; line-height: 1;
  }
  .product-type {
    position: absolute; left: 24px; top: 356px; color: var(--white);
    font-family: "Roboto Condensed", sans-serif;
  }
  .product-type .wash { font-size: 42px; font-weight: 900; line-height: 1; }
  .product-type .claim { font-size: 23px; font-weight: 700; line-height: 1.1; }
  .product-type .finish { font-size: 12px; font-weight: 600; line-height: 1.25; }
  .tab {
    position: absolute; background: var(--tab-orange); color: var(--white);
    font-weight: 700; font-size: 14px; text-align: center;
    height: 24px; line-height: 24px; border-radius: 3px;
  }
  .tab-benefits { left: 650px; top: 12px; width: 104px; }
  .tab-directions { left: 588px; top: 214px; width: 110px; }
  .tab-notice { left: 588px; top: 318px; width: 110px; }
  .benefit-list {
    position: absolute; top: 44px; list-style: none;
    color: var(--white); font-size: 11.5px; line-height: 1.35;
  }
  .benefit-list li::before { content: "• "; }
  .benefit-list.col-a { left: 470px; width: 176px; }
  .benefit-list.col-b { left: 660px; width: 170px; }
  .safety {
    position: absolute; left: 470px; top: 154px; width: 360px;
    text-align: center; color: var(--navy); font-weight: 700;
    font-size: 14px; line-height: 1.25;
  }
  .directions, .notice {
    position: absolute; left: 466px; width: 364px;
    text-align: center; color: var(--white); font-size: 10px; line-height: 1.35;
  }
  .directions { top: 243px; }
  .notice { top: 347px; }
  .origin {
    position: absolute; left: 466px; top: 420px; width: 364px;
    text-align: center; color: var(--white); font-size: 11px; font-weight: 700;
  }
</style>
</head>
<body>
  <section class="label">
    <svg class="label-bg" viewBox="0 0 845 461" width="845" height="461" aria-hidden="true">
      <path d="M300 0 L845 0 L845 118 C690 160 520 150 420 100 C370 75 330 40 300 0 Z" fill="var(--brand-blue)"/>
      <path d="M320 0 C350 50 390 82 440 102" fill="none" stroke="var(--deep-blue)" stroke-width="4"/>
      <path d="M0 350 C200 345 330 300 430 250 C520 215 700 212 845 205 L845 461 L0 461 Z" fill="var(--brand-blue)"/>
      <path d="M0 347 C200 342 330 297 430 247 C520 212 700 209 845 202" fill="none" stroke="var(--deep-blue)" stroke-width="4"/>
    </svg>

    <div class="rv-visual" role="img" aria-label="Illustration of a Class A motorhome"></div>
    <div class="size-badge"><span class="qty">1</span><span class="unit">gallon jug</span></div>

    <p class="brand-name">Blue Harbor Gleam</p>
    <h1 class="product-title">PREMIUM RV</h1>
    <div class="product-type">
      <p class="wash">WASH &amp;WAX</p>
      <p class="claim">CLEANS &amp;PROTECTS</p>
      <p class="finish">FOR STREAK-FREE FINISH<br>FOR ALL RV</p>
    </div>

    <div class="tab tab-benefits">Benefits</div>
    <ul class="benefit-list col-a">
      <li>Developed for Use With Foam Gun or Bucket with Water</li>
      <li>Safe for All RV Exteriors</li>
      <li>Protective Wax Formula</li>
    </ul>
    <ul class="benefit-list col-b">
      <li>Enhanced Shine</li>
      <li>Water Repellent</li>
      <li>Streak Free Rinse</li>
      <li>UV Protection</li>
    </ul>

    <p class="safety">Keep from freezing<br>Keep Out of Reach of Children<br>Hazardous Ingredients: NONE.</p>

    <div class="tab tab-directions">Directions</div>
    <p class="directions">Pour Concentrate into Foam Gun Bottle<br>OR<br>1 Part Wash &amp; Wax / 3 Parts Water in bucket. Apply soap to one side of RV at a time and use carwash brush to easily loosen road film and rinse clean.</p>

    <div class="tab tab-notice">NOTICE</div>
    <p class="notice">The seller and/or manufacturer assumes no responsibility for damage or injury resulting from misuse of this product. No warranties, expressed or implied, are given for the performance or safety of this product.</p>
    <p class="origin">MADE IN USA</p>
  </section>
</body>
</html>
```